Harbor Learning Growth Services (HLGS)

BI-Fold Brochure
1st page of brochure I want my name and logo of my company. I also want my picture Marisol Dunleavy - CEO and Gerald Whitcombe - Executive Director with descriptions of ourselves.
2nd page of brochure names our Professional Development that HLGS offers. We have 9 different PD's and are willing to provide PD on the weekend as well.
3rd page of brochure talks about our mentoring program with a paragraph of "why" mentoring is important for At-Risk children ages 8-18. "Compass Keepers Program" for males and "Daughters of Purpose & Grace" (D.O.P.G.) for our females. Mentioning our 4 different programs - "Summer School Program", "After School Program", In School Youth/Mentor Program", and "In School Youth/Adult Mentor Program with P.D.".
4th page of brochure will be Testimonials and 2 pictures of our mentors with children. Phone numbers, website, email address.

Target Market(s)

We are looking for school districts/ companies/corporations/wealthy individuals that are interested in sponsoring our programs for At-Risk youth and for sponsoring At-Risk schools that are failing.

Font styles to use
Serif

Colors

Designer to choose colors to be used in the design.

Requirements
Must have
• When people are looking at the HLGS brochure I want them to have a "good feeling". What HLGS consultants do are to "uplift" the individuals and schools that we work with. All HLGS consultants are college educated professionals and all of HLGS mentors for At-Risk are individuals who were mentored themselves when young.
Nice to have
• Your input - ideas!

```html
<!DOCTYPE html>
<html lang="en">
<head>
<meta charset="utf-8">
<title>Harbor Learning Growth Services — Brochure Cover</title>
<link href="https://fonts.googleapis.com/css2?family=Montserrat:wght@300;400;700;800&display=swap" rel="stylesheet">
<style>
  :root {
    --backdrop: #5a5a5c;
    --paper: #ffffff;
    --sky-blue: #3f74c9;
    --sky-blue-deep: #2f63b8;
    --navy: #0e3571;
    --slate: #8b8c8f;
    --mist-light: #f4f4f4;
    --mist-dark: #c9c9cb;
    --suit-dark: #1e2433;
    --ink: #1d1d1f;
    --link-blue: #3a6fc4;
  }
  * { margin: 0; padding: 0; box-sizing: border-box; }
  html, body { width: 854px; height: 1200px; overflow: hidden; }
  body {
    background: var(--backdrop);
    font-family: "Montserrat", Arial, sans-serif;
    position: relative;
  }
  .cover {
    position: absolute;
    left: 72px; top: 86px;
    width: 710px; height: 1008px;
    background: var(--paper);
    overflow: hidden;
  }
  .cover-shapes { position: absolute; inset: 0; }

  .brand {
    position: absolute;
    left: 250px; top: 64px;
    height: 112px;
    display: flex; align-items: center;
  }
  .brand-mark {
    font-weight: 800;
    font-size: 40px;
    letter-spacing: 5px;
    color: var(--navy);
    padding-right: 16px;
  }
  .brand-divider {
    width: 2px; height: 112px;
    background: var(--navy);
    margin-right: 16px;
  }
  .brand-name {
    font-weight: 700;
    font-size: 22px;
    line-height: 30px;
    color: var(--navy);
    white-space: nowrap;
  }

  .person-caption { position: absolute; line-height: 1.2; white-space: nowrap; }
  .person-name { font-weight: 700; font-size: 17px; }
  .person-role { font-weight: 300; font-size: 15px; }
  .caption-ceo { left: 265px; top: 442px; color: var(--paper); }
  .caption-director { left: 274px; top: 820px; color: var(--ink); }
  .caption-director .person-role { font-weight: 400; }

  .tagline {
    position: absolute;
    left: 537px; top: 551px;
    font-weight: 700;
    font-size: 19px;
    line-height: 25px;
    color: var(--paper);
    white-space: nowrap;
  }
  .website {
    position: absolute;
    right: 39px; top: 942px;
    font-weight: 700;
    font-size: 21px;
    color: var(--link-blue);
  }
</style>
</head>
<body>
  <main class="cover">
    <svg class="cover-shapes" width="710" height="1008" viewBox="0 0 710 1008">
      <defs>
        <linearGradient id="ceo-photo-tone" x1="0.8" y1="0" x2="0.15" y2="1">
          <stop offset="0" stop-color="#2f63b8"/>
          <stop offset="0.5" stop-color="#4a7ccf"/>
          <stop offset="0.75" stop-color="#7d8fb0"/>
          <stop offset="1" stop-color="#1e2433"/>
        </linearGradient>
        <linearGradient id="director-photo-tone" x1="0.6" y1="0" x2="0.2" y2="1">
          <stop offset="0" stop-color="#f2f2f2"/>
          <stop offset="0.45" stop-color="#cfcfd1"/>
          <stop offset="0.75" stop-color="#6b6e76"/>
          <stop offset="1" stop-color="#1e2433"/>
        </linearGradient>
      </defs>
      <polygon class="photo-ceo" role="img" aria-label="Portrait photo of Marisol Dunleavy, Chief Executive Officer, on a blue backdrop"
               points="0,164 498,457 0,744" fill="url(#ceo-photo-tone)"/>
      <polygon class="panel-navy" points="498,481 498,819 206,651" fill="var(--navy)"/>
      <polygon class="photo-director" role="img" aria-label="Portrait photo of Gerald Whitcombe, Executive Director, on a light grey backdrop"
               points="0,762 178,660 492,839 202,1008 0,1008" fill="url(#director-photo-tone)"/>
      <polygon class="accent-sky" points="518,457 710,343 710,566" fill="var(--sky-blue)"/>
      <polygon class="panel-slate" points="516,481 710,594 710,707 516,819" fill="var(--slate)"/>
    </svg>

    <header class="brand">
      <span class="brand-mark">HLGS</span>
      <span class="brand-divider"></span>
      <div class="brand-name">Harbor<br>Learning<br>Growth<br>Services</div>
    </header>

    <div class="person-caption caption-ceo">
      <div class="person-name">Marisol Dunleavy</div>
      <div class="person-role">Chief Executive Officer</div>
    </div>

    <div class="person-caption caption-director">
      <div class="person-name">Gerald Whitcombe</div>
      <div class="person-role">Executive Director</div>
    </div>

    <p class="tagline">The best<br>way to get<br>connected<br>with<br>consultants<br>in your<br>industry!</p>

    <p class="website">hlgsgrowth.com</p>
  </main>
</body>
</html>
```